Electrical needs letterhead design

Need a letterhead design for an electrical company. Using the same colours as to what are used in the logo.
After a modern design.

Want the logo in top right or top left.

Must include...

ABN 61 842 307 194
PHONE 0492357018
www.voltarnex.com.au
ben@voltarnex.com.au

'ABN' and 'PHONE' in bold.

Keep it basic. Logo top left, details either next to it or far right corner. Dont want any other objects included.

```html
<!DOCTYPE html>
<html lang="en">
<head>
<meta charset="utf-8">
<title>Voltarnex Electrical Solutions – Letterhead</title>
<link rel="stylesheet" href="https://fonts.googleapis.com/css2?family=Open+Sans:wght@400;600&family=Arimo:wght@400;700&display=swap">
<style>
  :root {
    --backdrop: #e6e6e6;
    --brand-red: #e0402c;
    --brand-dark: #9b1f1a;
    --paper: #ffffff;
    --ink: #3a3a3a;
    --ink-soft: #7a7a7a;
  }
  * { margin: 0; padding: 0; box-sizing: border-box; }
  html, body {
    width: 1200px;
    height: 1000px;
    overflow: hidden;
    background: var(--backdrop);
  }
  .canvas {
    position: relative;
    width: 1200px;
    height: 1000px;
  }

  /* Reverse side */
  .sheet-reverse {
    position: absolute;
    left: 45px;
    top: 126px;
    width: 637px;
    height: 821px;
    background: var(--brand-red);
  }
  .reverse-mark {
    position: absolute;
    left: 0;
    width: 472px;
    top: 330px;
    display: flex;
    align-items: center;
    justify-content: center;
    gap: 16px;
  }
  .reverse-mark .dot {
    width: 34px;
    height: 34px;
    border-radius: 50%;
    background: var(--paper);
  }
  .reverse-mark .name {
    font-family: "Open Sans", sans-serif;
    font-weight: 600;
    font-size: 58px;
    color: var(--paper);
    letter-spacing: 0.5px;
  }

  /* Front letterhead */
  .sheet-front {
    position: absolute;
    left: 517px;
    top: 47px;
    width: 637px;
    height: 822px;
    background: var(--paper);
  }
  .brand {
    position: absolute;
    left: 110px;
    top: 48px;
  }
  .brand-name {
    display: flex;
    align-items: center;
    gap: 6px;
    font-family: "Open Sans", sans-serif;
    font-weight: 400;
    font-size: 29px;
    line-height: 1;
    color: var(--brand-dark);
  }
  .brand-name .dot {
    width: 9px;
    height: 9px;
    border-radius: 50%;
    background: var(--brand-dark);
  }
  .brand-tagline {
    margin-top: 3px;
    margin-left: 2px;
    font-family: "Open Sans", sans-serif;
    font-size: 6px;
    letter-spacing: 2.6px;
    color: var(--ink-soft);
  }

  .contact {
    position: absolute;
    left: 494px;
    top: 89px;
    font-family: "Arimo", sans-serif;
    font-size: 7px;
    line-height: 10px;
    color: var(--ink);
  }
  .contact .abn { margin-bottom: 7px; font-weight: 700; }
  .contact .abn .label { color: var(--brand-red); }
  .contact .row { display: flex; align-items: center; gap: 4px; }
  .contact .phone { font-weight: 700; }
  .contact .email { color: var(--ink-soft); }
  .contact .web { font-weight: 700; color: var(--brand-dark); }
  .contact svg { width: 6px; height: 6px; flex: none; }
</style>
</head>
<body>
<main class="canvas">
  <section class="sheet-reverse" aria-label="Letterhead reverse side">
    <div class="reverse-mark">
      <span class="dot"></span>
      <span class="name">Voltarnex</span>
    </div>
  </section>

  <section class="sheet-front" aria-label="Letterhead front side">
    <header class="brand">
      <div class="brand-name"><span class="dot"></span>Voltarnex</div>
      <div class="brand-tagline">ELECTRICAL SOLUTIONS</div>
    </header>

    <address class="contact">
      <div class="abn"><span class="label">ABN:</span> 61 842 307 194</div>
      <div class="row phone">
        <svg viewBox="0 0 10 10" aria-hidden="true"><path fill="#9b1f1a" d="M2 0.5 L3.6 2.8 L2.6 3.8 Q3.6 6 6.2 7.4 L7.2 6.4 L9.5 8 L8.4 9.5 Q1.5 8 0.5 1.6 Z"/></svg>
        0492357018
      </div>
      <div class="row email">
        <svg viewBox="0 0 10 8" aria-hidden="true"><rect width="10" height="8" fill="#9b1f1a"/><path d="M0.5 0.8 L5 4.5 L9.5 0.8" stroke="#fff" stroke-width="0.9" fill="none"/></svg>
        ben@voltarnex.com.au
      </div>
      <div class="web">www.voltarnex.com.au</div>
    </address>
  </section>
</main>
</body>
</html>
```